Meridian Lodging Partners

An Editable Business Card Template For MLP & MLH
Similar or Different Design

418 W. Harlan Brookside Pkwy.
Suite 2270
Irving, TX 75091

```html
<!DOCTYPE html>
<html lang="en">
<head>
<meta charset="utf-8">
<title>Meridian Lodging Partners – Business Card</title>
<link rel="stylesheet" href="https://fonts.googleapis.com/css2?family=EB+Garamond:wght@400;600;700&family=Cinzel:wght@400&display=swap">
<style>
  :root {
    --backdrop: #ababab;
    --card-white: #ffffff;
    --card-cream: #faf8f6;
    --brand-red: #850008;
    --brand-red-light: #b4262c;
    --ink: #111111;
    --slate-top: #8e9095;
    --slate-bottom: #7d7f84;
    --on-dark: #ffffff;
  }
  * { margin: 0; padding: 0; box-sizing: border-box; }
  html, body { width: 1200px; height: 1000px; overflow: hidden; }
  body {
    background: var(--backdrop);
    font-family: "EB Garamond", Georgia, serif;
    position: relative;
  }
  .card {
    position: absolute;
    left: 294px;
    width: 613px;
    height: 351px;
    border-radius: 22px;
    overflow: hidden;
    box-shadow: 0 18px 30px rgba(0,0,0,0.28);
  }
  .card--front { top: 118px; background: var(--card-white); }
  .card--back { top: 532px; background: var(--card-cream); }

  .brand-seal {
    position: absolute;
    left: 29px; top: 17px;
    width: 260px; height: 260px;
    border-radius: 50%;
    background: var(--brand-red-light);
    display: flex; align-items: center; justify-content: center;
  }
  .brand-seal__name {
    color: var(--on-dark);
    font-weight: 600;
    font-size: 28px;
    line-height: 1.15;
    text-align: center;
  }
  .partner-name {
    position: absolute;
    color: var(--ink);
    font-weight: 600;
    font-size: 18px;
    line-height: 1.1;
  }
  .card--front .partner-name { left: 326px; top: 62px; }

  .contact { position: absolute; left: 326px; top: 134px; color: var(--ink); }
  .contact__name { font-size: 34px; font-weight: 700; line-height: 1; }
  .contact__title { font-size: 18px; font-weight: 600; margin-top: 8px; }
  .contact__lines { font-size: 22px; line-height: 29px; margin-top: 6px; }

  .band {
    position: absolute; left: 0; bottom: 0;
    width: 100%; height: 45px;
    background: var(--brand-red);
    color: var(--on-dark);
    display: flex; align-items: center; justify-content: center;
  }
  .band--tagline { font-family: "Cinzel", "Times New Roman", serif; font-size: 25px; letter-spacing: 0.5px; }
  .band--web { font-size: 27px; font-weight: 700; }

  .back-panels { position: absolute; left: 0; top: 0; }

  .office { position: absolute; left: 0; top: 40px; width: 264px; text-align: center; color: var(--brand-red); font-size: 27px; line-height: 34px; font-weight: 600; }
  .office-mark {
    position: absolute; left: 61px; top: 110px;
    width: 123px; height: 88px; background: var(--card-white);
    display: flex; align-items: center; justify-content: center;
    color: var(--ink); font-size: 18px; font-weight: 600; text-align: center; line-height: 1.1;
  }
  .address { position: absolute; left: 25px; top: 206px; font-size: 16px; line-height: 22px; font-weight: 600; color: var(--ink); white-space: nowrap; }

  .services { position: absolute; left: 302px; top: 30px; color: var(--on-dark); }
  .services__heading { font-size: 19.5px; font-weight: 700; line-height: 24px; }
  .services__list { list-style: none; font-size: 18px; }
  .services__list li { position: absolute; white-space: nowrap; }
  .services__list li::before { content: "• "; }
</style>
</head>
<body>
  <section class="card card--front" aria-label="Business card front">
    <div class="brand-seal"><p class="brand-seal__name">Meridian<br>Lodging<br>Housing</p></div>
    <p class="partner-name">Meridian Lodging<br>Partners</p>
    <div class="contact">
      <p class="contact__name">Dana Whitcombe</p>
      <p class="contact__title">Sales Manager</p>
      <p class="contact__lines">DWhitcombe@meridianlp.com<br>O: 214-555-0186<br>C: 480-555-0143</p>
    </div>
    <div class="band band--tagline">Oil Field Lodging Made Simple</div>
  </section>

  <section class="card card--back" aria-label="Business card back">
    <svg class="back-panels" width="613" height="351" viewBox="0 0 613 351" aria-hidden="true">
      <defs>
        <linearGradient id="slate" x1="0" y1="0" x2="0" y2="1">
          <stop offset="0" stop-color="var(--slate-top)"/>
          <stop offset="1" stop-color="var(--slate-bottom)"/>
        </linearGradient>
      </defs>
      <polygon points="291,0 613,0 613,306 256,306" fill="url(#slate)"/>
      <polygon points="283,0 292,0 256,306 247,306" fill="var(--brand-red)"/>
    </svg>
    <p class="office">Corporate Office<br>214-555-0186</p>
    <div class="office-mark">Meridian<br>Lodging<br>Partners</div>
    <p class="address">418 W. Harlan Brookside Pkwy.<br>Suite 2270<br>Irving, TX 75091</p>
    <div class="services">
      <p class="services__heading">Experienced Provider To Oil, Gas,<br>Energy &amp; Construction Industries</p>
      <ul class="services__list">
        <li style="left:-4px;top:70px">Consolidated Billing</li>
        <li style="left:-10px;top:108px">Full Service Corporate Lodging</li>
        <li style="left:-14px;top:146px">Live Customer Support 24/7/365</li>
        <li style="left:-20px;top:187px">Proven Track Record Of Performance</li>
        <li style="left:-24px;top:223px">Best Negotiated Rates &amp; No Additional Fees</li>
      </ul>
    </div>
    <div class="band band--web">www.MLPOilField.com</div>
  </section>
</body>
</html>
```